Brindle cards

I am in the auto motive, transportation business I would like a business card that is Something cool, modern edgy, having to do with car culture. I offer towing service for high and exotic cars. I also provide towing for collisions and car accidents. I offer open and enclosed transport nationwide.

Target Market(s)

Car culture people high end auto collectors

Industry/Entity Type

Towing car carrier

Contact Information for Business Card

My company colors black yellow and silver

Font styles to use
Serif

```html
<!DOCTYPE html>
<html lang="en">
<head>
<meta charset="utf-8">
<title>Brindle Business Cards</title>
<link rel="stylesheet" href="https://fonts.googleapis.com/css2?family=Montserrat:wght@400;500;800&display=swap">
<style>
  :root {
    --black: #050505;
    --ink: #111111;
    --yellow: #fcc520;
    --white: #ffffff;
    --paper: #f4f4f4;
    --silver: #d9d9d9;
    --backdrop: #8a8a8a;
  }
  * { box-sizing: border-box; margin: 0; padding: 0; }
  html, body { width: 1200px; height: 1200px; overflow: hidden; }
  body {
    background: var(--backdrop);
    font-family: "Montserrat", sans-serif;
    position: relative;
  }
  .card {
    position: absolute;
    left: 250px;
    width: 700px;
    height: 400px;
    border-radius: 28px;
    overflow: hidden;
    box-shadow: 0 14px 30px rgba(0,0,0,.35);
  }
  .card-front { top: 150px; background: var(--paper); }
  .card-back { top: 650px; background: var(--black); }

  .front-split { position: absolute; inset: 0; width: 100%; height: 100%; }

  .contact {
    position: absolute;
    left: 60px;
    top: 150px;
    color: var(--white);
  }
  .identity {
    border-left: 4px solid var(--yellow);
    padding-left: 14px;
    margin-bottom: 30px;
  }
  .person-name {
    color: var(--yellow);
    font-weight: 500;
    font-size: 36px;
    letter-spacing: 1px;
    line-height: 1;
  }
  .person-role {
    font-size: 15px;
    letter-spacing: 1px;
    margin-top: 6px;
  }
  .contact-list { list-style: none; }
  .contact-item {
    display: flex;
    align-items: center;
    gap: 14px;
    font-size: 21px;
    margin-bottom: 12px;
  }
  .contact-icon { width: 24px; height: 24px; flex: none; }

  .wordmark {
    position: absolute;
    font-weight: 800;
    text-transform: uppercase;
    letter-spacing: 3px;
    line-height: 1;
  }
  .wordmark-front {
    right: 70px;
    top: 175px;
    font-size: 50px;
    color: var(--ink);
  }
  .wordmark-back {
    left: 0; right: 0;
    top: 172px;
    text-align: center;
    font-size: 64px;
    color: var(--silver);
  }
  .back-glow {
    position: absolute;
    inset: 0;
    background: radial-gradient(circle at 50% 45%, #2c2c2c 0%, #141414 45%, var(--black) 80%);
  }
</style>
</head>
<body>
  <section class="card card-front">
    <svg class="front-split" viewBox="0 0 700 400" preserveAspectRatio="none" aria-hidden="true">
      <polygon points="0,0 290,0 380,400 0,400" fill="var(--black)"/>
      <polygon points="290,0 302,0 392,400 380,400" fill="var(--yellow)"/>
    </svg>
    <div class="contact">
      <div class="identity">
        <h1 class="person-name">JOHN DOE</h1>
        <p class="person-role">POSITION</p>
      </div>
      <ul class="contact-list">
        <li class="contact-item">
          <svg class="contact-icon" viewBox="0 0 24 24" aria-hidden="true"><path fill="var(--yellow)" d="M6.6 10.8a15 15 0 0 0 6.6 6.6l2.2-2.2c.3-.3.7-.4 1-.2 1.1.4 2.3.6 3.6.6.6 0 1 .4 1 1V20c0 .6-.4 1-1 1A17 17 0 0 1 3 4c0-.6.4-1 1-1h3.5c.6 0 1 .4 1 1 0 1.3.2 2.5.6 3.6.1.3 0 .7-.2 1z"/></svg>
          (000) 000 0000
        </li>
        <li class="contact-item">
          <svg class="contact-icon" viewBox="0 0 24 24" aria-hidden="true"><rect x="2" y="5" width="20" height="14" fill="var(--yellow)"/><path d="M2 5l10 8 10-8" fill="none" stroke="var(--black)" stroke-width="1.6"/></svg>
          email@youremail.com
        </li>
        <li class="contact-item">
          <svg class="contact-icon" viewBox="0 0 24 24" aria-hidden="true"><g fill="none" stroke="var(--yellow)" stroke-width="1.8"><circle cx="12" cy="12" r="10"/><ellipse cx="12" cy="12" rx="4.5" ry="10"/><path d="M2 12h20M4 7h16M4 17h16"/></g></svg>
          www.yourwebsite.com
        </li>
      </ul>
    </div>
    <p class="wordmark wordmark-front">Brindle</p>
  </section>

  <section class="card card-back">
    <div class="back-glow" role="img" aria-label="Dark radiating light rays behind the company name"></div>
    <p class="wordmark wordmark-back">Brindle</p>
  </section>
</body>
</html>
```